Business card design for Allied Healthcare provider

We would like a design for front and back of business cards. The design must resonate with all levels of customers from patients, to other health providers and medical. Must also resonate with corporate customers

Target Market(s)

patients, medical practitioners, other health providers and corporate.

Industry/Entity Type

healthcare

Contact Information for Business Card

name, logo, phone and fax numbers, email, website

Requirements
Must have
• not allowing me to change this, but the card must be double sided!! Please take note
Nice to have
• a fresh yet bold design to catch attention.

```html
<!DOCTYPE html>
<html lang="en">
<head>
<meta charset="utf-8">
<title>carewell business cards</title>
<link rel="stylesheet" href="https://fonts.googleapis.com/css2?family=Poppins:wght@400;500;600;700&display=swap">
<style>
  :root {
    --navy: #1b2b5a;
    --gold: #f6b82a;
    --white: #ffffff;
    --ink: #1b2b5a;
    --stage: #dfe1e6;
  }
  * { box-sizing: border-box; margin: 0; padding: 0; }
  html, body {
    width: 1200px; height: 801px; overflow: hidden;
    background: var(--stage);
    font-family: "Poppins", sans-serif;
  }
  .sheet {
    width: 1200px; height: 801px;
    display: flex; align-items: center; justify-content: center; gap: 40px;
  }
  .card {
    position: relative;
    width: 520px; height: 300px;
    border-radius: 20px;
    overflow: hidden;
    box-shadow: 0 10px 30px rgba(20, 30, 60, 0.18);
  }

  /* Back */
  .card--back {
    background: var(--navy);
    display: flex; align-items: center; justify-content: center;
  }
  .brand { display: flex; align-items: center; gap: 12px; }
  .brand__dot { width: 34px; height: 34px; border-radius: 50%; flex: none; }
  .brand__name { font-weight: 600; line-height: 1; letter-spacing: 0.5px; }
  .card--back .brand__dot { background: var(--gold); }
  .card--back .brand__name { color: var(--white); font-size: 52px; }
  .brand__block { display: flex; flex-direction: column; align-items: flex-end; }
  .tagline {
    color: var(--gold); font-size: 15px; font-weight: 400;
    letter-spacing: 0.4px; margin-top: 2px; white-space: nowrap;
  }

  /* Front */
  .card--front { background: var(--white); }
  .card--front .brand {
    position: absolute; top: 44px; left: 150px;
  }
  .card--front .brand__dot { background: var(--navy); width: 28px; height: 28px; }
  .card--front .brand__name { color: var(--navy); font-size: 40px; }

  .person { position: absolute; left: 38px; top: 128px; }
  .person__name { color: var(--ink); font-size: 24px; font-weight: 700; letter-spacing: 1px; white-space: nowrap; }
  .person__role { color: var(--gold); font-size: 14px; font-weight: 500; letter-spacing: 1px; margin-top: -2px; }
  .divider {
    position: absolute; left: 262px; right: 30px; top: 152px;
    height: 1px; background: var(--navy);
  }

  .contacts {
    position: absolute; left: 38px; top: 186px;
    list-style: none;
  }
  .contacts li {
    display: flex; align-items: center; gap: 10px;
    color: var(--ink); font-size: 13px; font-weight: 500;
    letter-spacing: 0.6px; height: 20px; white-space: nowrap;
  }
  .contacts svg { width: 13px; height: 13px; flex: none; }

  .address {
    position: absolute; right: 30px; top: 182px;
    text-align: right; color: var(--ink);
    font-size: 12px; font-weight: 500; line-height: 1.55; letter-spacing: 0.4px;
  }

  .edge { position: absolute; left: 0; bottom: 0; width: 100%; height: 18px; }
</style>
</head>
<body>
<main class="sheet">

  <section class="card card--back" aria-label="Card back">
    <div class="brand">
      <span class="brand__dot"></span>
      <div class="brand__block">
        <span class="brand__name">carewell</span>
        <span class="tagline">comfort · guidance · wellbeing</span>
      </div>
    </div>
  </section>

  <section class="card card--front" aria-label="Card front">
    <div class="brand">
      <span class="brand__dot"></span>
      <span class="brand__name">carewell</span>
    </div>

    <div class="person">
      <p class="person__name">Dana Whitfield</p>
      <p class="person__role">CEO</p>
    </div>
    <div class="divider"></div>

    <ul class="contacts">
      <li>
        <svg viewBox="0 0 16 16" aria-hidden="true"><path fill="#f6b82a" d="M3.5 1.5l2.3 0 1 3.2-1.6 1.2c.8 1.8 2.2 3.2 4 4l1.2-1.6 3.2 1v2.3c0 .8-.7 1.4-1.5 1.4C6.6 13 3 9.4 2.1 3c0-.8.6-1.5 1.4-1.5z"/></svg>
        0400318274
      </li>
      <li>
        <svg viewBox="0 0 16 16" aria-hidden="true"><rect x="4" y="1" width="8" height="4" fill="#f6b82a"/><rect x="1" y="5.5" width="14" height="6" rx="1" fill="#f6b82a"/><rect x="4" y="10" width="8" height="5" fill="#f6b82a" stroke="#fff" stroke-width="1"/></svg>
        0400318274
      </li>
      <li>
        <svg viewBox="0 0 16 16" aria-hidden="true"><rect x="1" y="3.5" width="14" height="9" rx="1" fill="#f6b82a"/><path d="M1.5 4l6.5 5 6.5-5" fill="none" stroke="#fff" stroke-width="1.2"/></svg>
        dana@carewellhealth.com
      </li>
      <li>
        <svg viewBox="0 0 16 16" aria-hidden="true"><circle cx="8" cy="8" r="6.5" fill="none" stroke="#f6b82a" stroke-width="1.4"/><ellipse cx="8" cy="8" rx="2.8" ry="6.5" fill="none" stroke="#f6b82a" stroke-width="1.2"/><path d="M1.5 8h13M2.5 5h11M2.5 11h11" stroke="#f6b82a" stroke-width="1.1"/></svg>
        www.carewellhealth.com
      </li>
    </ul>

    <p class="address">Po Box 418 Brookfield<br>Vic 3100 Australia</p>

    <svg class="edge" viewBox="0 0 520 18" preserveAspectRatio="none" aria-hidden="true">
      <polygon points="0,18 0,6 330,6 318,18" fill="#1b2b5a"/>
      <polygon points="330,6 520,0 520,18 318,18" fill="#f6b82a"/>
    </svg>
  </section>

</main>
</body>
</html>
```